Indian Takeaway Menu -

I would like to have double parallel fold A4 sheet menu.
A4 sheet cut in half and attached to the other half to make the sheet 4 small pages long.

Colors
abd036
ffffff

Requirements
Must have
• Please check new attachments - menu size and layout is not correct.
• I would like to add Dark brown colour. A4 sheet folded 4x Menu layout pocket size.
Nice to have
• Dark Brown - Parrot Green and very light Brown

```html
<!DOCTYPE html>
<html lang="en">
<head>
<meta charset="utf-8">
<title>Indian Takeaway Menu</title>
<link href="https://fonts.googleapis.com/css2?family=Kaushan+Script&family=Arimo:wght@400;700&display=swap" rel="stylesheet">
<style>
:root{
  --green:#abd036;
  --green-soft:#c9e27c;
  --white:#ffffff;
  --brown:#5a3215;
  --brown-light:#c9a77c;
  --text-dark:#3b2a14;
}
*{margin:0;padding:0;box-sizing:border-box}
html,body{width:1200px;height:212px;overflow:hidden;background:var(--white)}
body{font-family:"Arimo",Arial,sans-serif;font-size:5.3px;line-height:1.1}
.menu{display:flex;width:1200px;height:212px}
.panel{position:relative;width:300px;height:212px;display:flex;overflow:hidden}
.panel__body{flex:1;padding:2px 5px;overflow:hidden}
.panel--green .panel__body{background:var(--green);color:var(--white)}
.panel--light .panel__body{background:var(--white);color:var(--text-dark)}
.photo{width:52px;height:212px;background:linear-gradient(180deg,#a0522d,#d98c3a 35%,#7a8f3a 60%,#c45a23 85%,#5a3215)}
.title{font-family:"Kaushan Script",cursive;color:var(--brown);font-size:10px;font-weight:400;text-align:center;height:13px;line-height:13px;margin-bottom:3px;background:var(--green-soft)}
.frame{border:1px solid var(--white);height:190px;padding:2px;display:flex;gap:4px;overflow:hidden}
.panel--light .frame{border-color:var(--green)}
.col{flex:1;overflow:hidden}
.col--wide{flex:1.2}
.item{margin-bottom:1.5px}
.name{display:flex;justify-content:space-between;gap:2px}
.panel--light .name{color:#8fb51f}
.panel--green .name{color:var(--white)}
.section{color:var(--brown);font-weight:700;margin-bottom:1px}
.panel--green .section{color:var(--white)}
.price-list .row{display:flex;justify-content:space-between;border-bottom:1px dotted var(--brown-light);padding:2.4px 0}
.side-head{font-family:"Kaushan Script",cursive;font-weight:400;color:var(--brown);font-size:8px;text-align:center;line-height:1.15;margin-bottom:5px}
.veg-title{font-family:"Kaushan Script",cursive;font-weight:400;color:var(--brown);font-size:10px;margin-bottom:3px}
</style>
</head>
<body>
<main class="menu">

<section class="panel panel--green">
  <div class="panel__body">
    <h2 class="title">Starters</h2>
    <div class="frame">
      <div class="col">
        <div class="item"><div class="name"><span>Onion Bhajia</span><span>€4.50</span></div><div>Spinach &amp; onions fritters flavored with mild spices</div></div>
        <div class="item"><div class="name"><span>Vegetable Samosa 2</span><span>€4.50</span></div><div>Crispy pastry stuffed with potatoes, chick peas, green peas mixed with desi spices until golden.</div></div>
        <div class="item"><div class="name"><span>Aloo Tikki</span><span>€4.50</span></div><div>Cakes of fresh spinach and chana daal</div></div>
        <div class="item"><div class="name"><span>Veg Pakora</span><span>€5.00</span></div><div>Cauliflower, potato and broccoli, golden fried with gram flour batter</div></div>
        <div class="item"><div class="name"><span>Keema Singhara 2</span><span>€5.00</span></div><div>Spicy seasoned mince lamb in light pastry</div></div>
        <div class="item"><div class="name"><span>Chicken Tikka 3</span><span>€5.00</span></div><div>Tender chicken marinated overnight with yoghurt, spices charred in tandoor</div></div>
        <div class="item"><div class="name"><span>Seekh Kebab</span><span>€5.50</span></div><div>Skewered hand pounder lamb glazed in tandoor with green chilli &amp; black cardamom</div></div>
        <div class="item"><div class="name"><span>Chicken Pakora</span><span>€5.00</span></div><div>Boneless pieces of chicken coated in gram flour batter, with spices.</div></div>
      </div>
      <div class="col">
        <div class="item"><div class="name"><span>Chicken Wings 2,1</span><span>€5.00</span></div></div>
        <div class="item"><div class="name"><span>Tandoori Mix Meat Platter 3</span><span>€9.50</span></div><div>Our special tandoori assortment of tandoori chicken on bone, seekh kebab and chicken tikka</div></div>
        <div class="item"><div class="name"><span>Mix Veg platter 2</span><span>€6.50</span></div><div>Veg Samosa, Onion Bhaji, Veg Pakora</div></div>
        <div class="item"><div class="name"><span>Doner Kebab 2,3,6</span><span>€8.00</span></div><div>Stripes of minced chicken &amp; beef served with garlic mayo, chilli sauce &amp; mixed salad &amp; wrapped in naan.</div></div>
        <div class="item"><div class="name"><span>Chicken Tikka Kebab 2,3,6</span><span>€8.00</span></div><div>Chicken breast marinated in spices, barbecued served with garlic mayo, chilli sauce &amp; mixed salad &amp; wrapped in naan</div></div>
        <div class="item"><div class="name"><span>Mix Kebab 2,3,6</span><span>€8.00</span></div><div>Pieces of chicken tikka &amp; donner meat with garlic mayo, sweet chilli &amp; salad wrapped in naan bread</div></div>
        <div class="item"><div class="name"><span>Garlic Chips</span><span>€4.00</span></div></div>
      </div>
    </div>
  </div>
  <div class="photo" role="img" aria-label="Photographs of starters and spices"></div>
</section>

<section class="panel panel--light">
  <div class="panel__body">
    <h2 class="title">Chef Rana's Special Curries</h2>
    <div class="frame">
      <div class="col">
        <div class="item"><div class="name"><span>Butter Murgh 3,5</span><span>10.50</span></div><div>Chicken cooked in tandoor mixed with rich tomato creamy cashew sauce, splash of cream with hint of honey &amp; dry fenugreek.</div></div>
        <div class="item"><div class="name"><span>Laal Maas</span><span>11.50</span></div><div>Traditional rajasthani lamb cooked with garlic and ginger, degi chilli powder, tomatoes finished with star aniseed and clove powder</div></div>
        <div class="item"><div class="name"><span>Shahi Veg Kofta 3,5</span><span>10.00</span></div><div>Handmade veg and panner dumplings simmered in tomato sauce, musky fenugreek sauce finished with touch of honey and cream.</div></div>
        <div class="item"><div class="name"><span>Kerala Prawn 14</span><span>12.00</span></div><div>Delicacy of kerala spices, tomato and red onion gravy finished with touch of fresh coconut milk.</div></div>
      </div>
      <div class="col col--wide">
        <div class="section">Chicken Dishes</div>
        <div class="item"><div class="name"><span>Punjabi Saag 3</span><span>9.95</span></div><div>Chicken cooked with spinach, ginger, garlic, fresh cream &amp; tempered with Punjabi tarka.</div></div>
        <div class="item"><div class="name"><span>Royale Korm 3,5</span><span>€9.95</span></div><div>Breast of chicken cooked in a rich creamy sauce with saffron &amp; coconut, probably most popular among Irish.</div></div>
        <div class="item"><div class="name"><span>Saffron House Chicken Curry 3,4,5</span><span>€9.95</span></div><div>Traditional curry cooked with coconut, mustard seed, cashews and curry leaves.</div></div>
        <div class="item"><div class="name"><span>Chicken Karahi</span><span>€9.95</span></div><div>Boneless chicken. Prepared in Deg with peppers, onion, tomatoes and Indian whole spices.</div></div>
        <div class="item"><div class="name"><span>Chicken Tikka Masala 3</span><span>9.95</span></div><div>Chicken roasted in clayoven and simmered in smooth creamy tomato sauce with palm crushed fenugreek leaves and jaggery</div></div>
        <div class="item"><div class="name"><span>South Indian Garlic Chilli</span><span>€9.95</span></div><div>Chicken cooked in south Indian style and loaded with garlic, ground spices, fresh herbs.</div></div>
        <div class="item"><div class="name"><span>Chicken Dahiwala 3</span><span>€9.95</span></div><div>Amazingly spicy chicken curry cooked with yogurt, green chillies, ginger and herbs.</div></div>
        <div class="item"><div class="name"><span>Murgh Biryani 3,5,y</span><span>€9.95</span></div><div>Perfumed basmati rice with chicken cubes, nuts, golden onions and biryani spices, served with sauce.</div></div>
      </div>
    </div>
  </div>
  <div class="photo" role="img" aria-label="Photographs of curries and whole spices"></div>
</section>

<section class="panel panel--green">
  <div class="panel__body">
    <h2 class="title">Chef Rana's Special Curries</h2>
    <div class="frame">
      <div class="col">
        <div class="section">Prawn Dishes</div>
        <div class="item"><div class="name"><span>Prawn Masala 3</span><span>11.95</span></div><div>Prawns in a smooth creamy sauce flavoured with kasoori methi &amp; tandoori spices.</div></div>
        <div class="item"><div class="name"><span>Prawn Karahi</span><span>11.95</span></div><div>Prawns cooked with peppers, spring onion. Caramelised onion, tomatoes &amp; whole spices.</div></div>
        <div class="item"><div class="name"><span>Goan Prawn Curry 3,4,5</span><span>11.95</span></div><div>Fisherman's favourite prawn curry aromatic with coconut, mustard, nuts, curryleaves and spices from goa's costal area.</div></div>
        <div class="item"><div class="name"><span>Prawn Bhuna LF</span><span>€11.95</span></div><div>Prawns cooked in onions &amp; tomato with black pepper to bought together the kick of spices.</div></div>
        <div class="item"><div class="name"><span>Prawn Biryani 3,6,y</span><span>11.95</span></div><div>Pan fried prawn cooked with egg, green peas &amp; onion served with curry sauce.</div></div>
      </div>
      <div class="col">
        <div class="section">Lamb Dishes</div>
        <div class="item"><div class="name"><span>Lamb Madras</span><span>€10.95</span></div><div>The popular dish of madras cooked with plum tomato, degi chilli, coconut and finished with hint of lemon juice.</div></div>
        <div class="item"><div class="name"><span>Palak Gosht 3,y</span><span>€10.95</span></div><div>Pan-fried lamb pieces cooked with spinach, fresh herbs, ginger and touch of cream.</div></div>
        <div class="item"><div class="name"><span>Lamb Roganjosh</span><span>10.95</span></div><div>Slow cooked tender lamb in kashmiri style with fresh herbs and Himalayan spices.</div></div>
        <div class="item"><div class="name"><span>Lamb Kohlapuri 3,4,5</span><span>€10.95</span></div><div>Lamb dish from South Coast of India. Flavoured with yoghurt, nuts and coconut.</div></div>
        <div class="item"><div class="name"><span>Lamb Jalferzi 3,5</span><span>10.95</span></div><div>Lamb, tossed with cubes of onions, peppers flavored with crushed coriander seeds and dry fenugreek with hint of cream.</div></div>
        <div class="item"><div class="name"><span>Gosht Biryani 3,5,y</span><span>€11.00</span></div><div>Aged rice cooked with tender land brown onions, home made masala and accompanied with curry sauce.</div></div>
      </div>
    </div>
  </div>
  <div class="photo" role="img" aria-label="Photographs of prawn and lamb dishes"></div>
</section>

<section class="panel panel--light">
  <div class="panel__body">
    <div class="frame" style="border:none;height:208px">
      <div class="col col--wide">
        <h2 class="veg-title">Vegetable Dishes</h2>
        <div class="item"><div class="name"><span>Shahi Paneer 3,5</span><span>8.95</span></div><div>Indian cheese in semi-dry sauce.</div></div>
        <div class="item"><div class="name"><span>Subz Maloni Mild</span><span>8.95</span></div><div>Stir fried vegetables with ground spices.</div></div>
        <div class="item"><div class="name"><span>Dum Wale Aloo 3</span><span>8.95</span></div><div>Potatoes cooked with ginger, garlic, onions, yoghurt,&amp; curry leave with cumin Flavored.</div></div>
        <div class="item"><div class="name"><span>Karahi Paneer 3</span><span>8.95</span></div><div>Colorful curry is prepared using homemade Indian cheese (paneer)</div></div>
        <div class="item"><div class="name"><span>Saag Paneer 3,y</span><span>8.95</span></div><div>Pan fried cottage cheese &amp; spinach with kasoori methi &amp;fresh coriander</div></div>
        <div class="item"><div class="name"><span>Sambhar Vegetable Curry 4,y,v</span><span>8.95</span></div><div>Vegetable curry cooked with lentil, curry leaves, and mustard seeds</div></div>
        <div class="item"><div class="name"><span>Vegetable Biryani 3,5,y,v</span><span>8.95</span></div><div>Basmati Rice cooked with vegetables, fresh herbs, spices &amp; fried golden onion. Comes with curry sauce.</div></div>
      </div>
      <div class="col">
        <h2 class="side-head">Nan Bread &amp; Side Orders<br>All naan bread contains 2,3,6</h2>
        <div class="price-list">
          <div class="row"><span>Naan</span><span>€2.20</span></div>
          <div class="row"><span>Garlic Naan</span><span>€2.50</span></div>
          <div class="row"><span>Garlic Chilli naan</span><span>€3.00</span></div>
          <div class="row"><span>Peshwari Naan 5</span><span>€3.00</span></div>
          <div class="row"><span>Keema Naan</span><span>€3.00</span></div>
          <div class="row"><span>Coriander Naan</span><span>€2.50</span></div>
          <div class="row"><span>Chilli Cheese Naan 3</span><span>€3.00</span></div>
          <div class="row"><span>G.O.C</span><span>€3.00</span></div>
          <div class="row"><span>Boiled Basmati</span><span>€2.00</span></div>
          <div class="row"><span>Pilau Rice</span><span>€2.00</span></div>
          <div class="row"><span>Lemon Rice 4</span><span>€3.00</span></div>
          <div class="row"><span>Poppodum(2)</span><span>€2.50</span></div>
        </div>
      </div>
    </div>
  </div>
  <div class="photo" role="img" aria-label="Photographs of naan bread and vegetable dishes"></div>
</section>

</main>
</body>
</html>
```